Forking Well Buisiness card

needing a Business card for our company - Forking Well.
Forking well is co owned by Jess and Owen Marchetti (Husband and Wife)
Services Forking Well provides include:
Dietetic/nutrition Consultations, weight loss coaching programs, personal and group training, post injury rehab, health and nutrition presentations and Health Retreats.
Jess:
Accredited Practicing Dietitian & Personal trainer
Owen:
Personal trainer, rehab trainer & Strength and conditioning coach
At this stage the business cards will be made just for Jess.
She has a training studio in Armadale and Dietetics private practice in Richmond.
Mobile services are also available (i.e. meet at house or local cafe)

We need the card to look smart, modern and combine both nutrition and training.
We already have a logo which I will attach.
I was initial thinking i black background but am open to suggestions.

Target Market(s)

Health concious, People with money,

Industry/Entity Type

Nutrition

Contact Information for Business Card

Forking Well
Jess Marchetti
M: 0417390265
E: forkingwell@mailnest.com
W: www.forkingwell.com.au
Address:
Dietetics: Level 1, 583 Bellow Street
Kelvale VIC 3184
Training: Private Studio, behind 2087 Tamsin St
BRANWICK, VIC, 3152

Requirements
Must have
• Must have logo (see attached) please not the one we use is the top left (blue and green)
please note attachment is top left (green and blue)

needs to be clear to read - the font needs to be clear and sharp and the background cannot be too busy.eg funny patterns.
Could I please see a card with a line for 'appointment time/date:' possibly on the back. Would like to see what this looks like.
Jess Marchetti's Profile (side of card) must include "Accredited Practicing Dietitian" and "Personal Trainer."
I like when the services forking well provide are in dot form.
Nice to have
• would like the card to be 2 sides
first side:
Forking well logo - Large
services forking well provides: Dietetic/nutrition Consultations, weight loss coaching programs, personal and group training, post injury rehab, health and nutrition presentations and Health Retreats.
web address
second side:
smaller logo
Details for Jess:
Accredited Practicing Dietitian
Personal Trainer
Contact Details:
M: 0417390265
E: forkingwell@mailnest.com
Address:
Kelvale VIC 3184
BRANWICK, VIC, 3152
Should not have
• Dietetic + nutrition consultations
Should say dietetic/nutrition consultations (first letter of words in capitals please)
Please write phone number as 0417 390 265
Not: 04 17 390265
- note numbers as 4, 3, 3.

```html
<!DOCTYPE html>
<html lang="en">
<head>
<meta charset="utf-8">
<title>Forking Well Business Card</title>
<link rel="stylesheet" href="https://fonts.googleapis.com/css2?family=Open+Sans:wght@400;600;700&display=swap">
<style>
  :root {
    --brand-blue: #1f56a3;
    --brand-green: #8cc63f;
    --ink: #2b2b2b;
    --paper: #ffffff;
    --backdrop: #dcdcdc;
  }
  * { box-sizing: border-box; margin: 0; padding: 0; }
  html, body { width: 1056px; height: 1200px; overflow: hidden; }
  body {
    background: var(--backdrop);
    font-family: "Open Sans", Arial, sans-serif;
    position: relative;
  }
  .card {
    position: absolute;
    left: 86px;
    width: 884px;
    height: 493px;
    background: var(--paper);
    box-shadow: 0 2px 6px rgba(0,0,0,0.18);
    overflow: hidden;
  }
  .card--front { top: 96px; }
  .card--back { top: 628px; }
  .card__bands { position: absolute; left: 0; top: 0; width: 884px; height: 493px; }
  .brand {
    position: absolute;
    display: flex;
    align-items: center;
    color: var(--brand-blue);
    font-weight: 400;
    white-space: nowrap;
  }
  .brand__dot { border-radius: 50%; background: var(--brand-green); flex: none; }
  .card--front .brand { left: 30px; top: 60px; font-size: 70px; gap: 22px; }
  .card--front .brand__dot { width: 110px; height: 110px; }
  .card--back .brand { right: 60px; top: 42px; font-size: 40px; gap: 14px; }
  .card--back .brand__dot { width: 58px; height: 58px; }
  .services {
    position: absolute;
    left: 358px;
    top: 198px;
    list-style: none;
    color: var(--brand-blue);
    font-size: 18.5px;
    line-height: 35px;
    letter-spacing: 0.3px;
    text-transform: uppercase;
  }
  .services li { position: relative; padding-left: 42px; }
  .services li::before {
    content: ""; position: absolute; left: 0; top: 13px;
    width: 7px; height: 7px; border-radius: 50%; background: var(--brand-blue);
  }
  .services li.services__wrap { line-height: 31px; }
  .web {
    position: absolute;
    color: var(--paper);
    font-weight: 700;
    font-size: 23px;
  }
  .card--front .web { left: 558px; top: 444px; }
  .card--back .web { left: 96px; top: 434px; }
  .profile { position: absolute; left: 96px; top: 84px; }
  .profile__name { color: var(--brand-blue); font-weight: 700; font-size: 28px; }
  .profile__titles { margin-top: 24px; color: var(--ink); font-size: 22px; line-height: 31px; }
  .contact {
    position: absolute; left: 66px; display: flex; align-items: center; gap: 10px;
    color: var(--brand-blue); font-weight: 700; font-size: 25px;
  }
  .contact--phone { top: 242px; }
  .contact--email { top: 300px; }
  .contact svg { flex: none; }
  .locations {
    position: absolute; right: 64px; top: 168px; text-align: right;
    color: var(--ink); font-size: 22px; line-height: 29px;
  }
  .locations__label { color: var(--brand-green); font-weight: 700; }
  .locations__block + .locations__block { margin-top: 26px; }
</style>
</head>
<body>
  <section class="card card--front">
    <svg class="card__bands" viewBox="0 0 884 493" aria-hidden="true">
      <polygon points="400,423 884,423 884,493 500,493" fill="var(--brand-blue)"/>
      <polygon points="0,451 476,451 526,493 0,493" fill="var(--brand-green)"/>
    </svg>
    <div class="brand"><span class="brand__dot"></span>Forking Well</div>
    <ul class="services">
      <li>Dietetic/Nutrition Consultations</li>
      <li>Weight Loss Coaching Programs</li>
      <li>Personal and Group Training</li>
      <li>Post Injury Rehab</li>
      <li class="services__wrap">Health &amp; Nutrition Presentations<br>and Health Retreats</li>
    </ul>
    <div class="web">www.forkingwell.com.au</div>
  </section>

  <section class="card card--back">
    <svg class="card__bands" viewBox="0 0 884 493" aria-hidden="true">
      <polygon points="380,446 884,446 884,493 330,493" fill="var(--brand-green)"/>
      <polygon points="0,419 484,419 404,493 0,493" fill="var(--brand-blue)"/>
    </svg>
    <div class="brand"><span class="brand__dot"></span>Forking Well</div>
    <div class="profile">
      <div class="profile__name">Jess Marchetti</div>
      <div class="profile__titles">Accredited Practicing Dietitian<br>Personal Trainer</div>
    </div>
    <div class="contact contact--phone">
      <svg width="20" height="28" viewBox="0 0 20 28" aria-hidden="true">
        <rect x="2" y="1.5" width="16" height="25" rx="3" fill="none" stroke="var(--brand-blue)" stroke-width="2.5"/>
        <line x1="7" y1="22" x2="13" y2="22" stroke="var(--brand-blue)" stroke-width="2"/>
      </svg>
      <span>0417 390 265</span>
    </div>
    <div class="contact contact--email">
      <svg width="24" height="18" viewBox="0 0 24 18" aria-hidden="true">
        <rect x="1.5" y="1.5" width="21" height="15" fill="none" stroke="var(--brand-blue)" stroke-width="2"/>
        <polyline points="2,2 12,10 22,2" fill="none" stroke="var(--brand-blue)" stroke-width="2"/>
      </svg>
      <span>forkingwell@mailnest.com</span>
    </div>
    <div class="locations">
      <div class="locations__block">
        <div class="locations__label">Dietetics:</div>
        <div>Level 1, 583 Bellow Street</div>
        <div>Kelvale VIC 3184</div>
      </div>
      <div class="locations__block">
        <div class="locations__label">Training:</div>
        <div>Private Studio,</div>
        <div>behind 2087 Tamsin St</div>
        <div>BRANWICK, VIC, 3152</div>
      </div>
    </div>
    <div class="web">www.forkingwell.com.au</div>
  </section>
</body>
</html>
```